Velka Haven

Yoga and Pilates
I teach privates and small groups

Simple clean design 2-4 pages.
(Bookings will be though contacting me, so need for booking capabilities)

```html
<!DOCTYPE html>
<html lang="en">
<head>
<meta charset="utf-8">
<title>Velka Haven — Yoga and Pilates</title>
<link href="https://fonts.googleapis.com/css2?family=Outfit:wght@300;400;500;600;700;800;900&display=swap" rel="stylesheet">
<style>
:root{
  --pink:#e8877f;
  --pink-soft:#f6958d;
  --pink-card:#cf756f;
  --pink-button:#f38e87;
  --ink:#1e1e1e;
  --footer:#1b1b1b;
  --white:#ffffff;
  --grey-text:#5a5a5a;
}
*{margin:0;padding:0;box-sizing:border-box}
html,body{width:1200px;height:3884px;overflow:hidden}
body{font-family:"Outfit",sans-serif;color:var(--ink);background:var(--white);position:relative}
.abs{position:absolute}

/* Hero */
.hero{position:absolute;left:0;top:0;width:1200px;height:700px;overflow:hidden}
.hero-photo{position:absolute;inset:0;background:
  radial-gradient(ellipse at 85% 25%,rgba(246,196,120,.85),rgba(246,196,120,0) 45%),
  linear-gradient(180deg,#b9b3a8 0%,#a49c87 25%,#6f7d4a 45%,#5c7038 65%,#4e6230 100%)}
.hero-shade{position:absolute;inset:0;background:rgba(40,30,20,.18)}
.brand{position:absolute;font-weight:600;font-size:25px;color:var(--white);letter-spacing:-.3px}
.nav a{position:absolute;top:25px;color:var(--white);font-size:16px;font-weight:500;text-decoration:none}
.btn{position:absolute;background:var(--pink-button);color:var(--white);font-weight:600;display:flex;align-items:center;justify-content:center;box-shadow:4px 4px 0 rgba(255,255,255,.75)}
.hero-title{position:absolute;left:0;width:1200px;top:216px;text-align:center;color:var(--white);font-weight:900;font-size:86px;line-height:76px;letter-spacing:-1px}
.hero-sub{position:absolute;left:0;width:1200px;top:384px;text-align:center;color:var(--white);font-size:26px;font-weight:400}
.arrow{position:absolute;top:276px}

/* About */
.about-heading{position:absolute;left:172px;top:740px;font-weight:800;font-size:48px;line-height:57px}
.about-heading span{color:var(--pink)}
.about-note{position:absolute;left:172px;top:929px;width:260px;font-size:15px;line-height:22px}
.photo{position:absolute}
.about-text{position:absolute;left:764px;top:729px;width:280px;font-size:14.5px;line-height:26px;color:#333}

/* Weekly classes */
.classes{position:absolute;left:0;top:1253px;width:1200px;height:938px;background:var(--pink)}
.section-title{position:absolute;left:0;width:1200px;text-align:center;font-weight:800;font-size:48px}
.section-lead{position:absolute;left:0;width:1200px;text-align:center;font-size:15.5px;line-height:27px}
.card{position:absolute;width:268px;height:311px;background:var(--pink-card);border-radius:6px;overflow:hidden}
.card-photo{height:169px}
.card h3{margin:17px 0 0 16px;font-size:20px;font-weight:600;color:var(--white)}
.card p{margin:5px 16px 0 16px;font-size:14.5px;line-height:20px;color:#fbe3e0}
.card .more{position:absolute;left:16px;top:267px;color:var(--white);font-size:15px;font-weight:600;border-bottom:1px solid var(--white);padding-bottom:2px}

/* Benefits */
.benefits{position:absolute;left:0;top:2191px;width:1200px;height:756px;background:linear-gradient(180deg,#ffffff 0%,#ffffff 40%,#eef0f3 65%,#f7f7f8 100%)}
.benefit{position:absolute;width:220px}
.benefit h4{font-size:20px;font-weight:500;color:var(--ink)}
.benefit p{font-size:15px;line-height:21px;color:var(--grey-text);margin-top:3px}
.icon-dot{position:absolute;width:78px;height:78px;border-radius:50%;background:var(--pink);display:flex;align-items:center;justify-content:center;box-shadow:0 0 0 5px rgba(232,135,127,.25)}

/* Contact */
.contact{position:absolute;left:0;top:2947px;width:1200px;height:650px;background:var(--pink)}
.info-dot{position:absolute;width:58px;height:58px;border-radius:50%;background:var(--white);display:flex;align-items:center;justify-content:center}
.info{position:absolute;color:var(--white);font-size:13.5px;line-height:22px}
.info b{font-weight:700;font-size:14px;display:block}
.form-panel{position:absolute;left:200px;top:229px;width:800px;height:326px;background:var(--pink-soft)}
.field{position:absolute;background:var(--white);border:1px solid #e6d2d0;font-size:14px;color:#444;padding:10px 9px;font-family:inherit}

/* Footer */
.footer{position:absolute;left:0;top:3540px;width:1200px;height:344px}
.foot-col h5{font-size:14px;font-weight:600;color:var(--white)}
.foot-list{list-style:none}
.foot-list li{font-size:14px;color:#d9d9d9;margin-top:20px;padding-left:20px;position:relative}
.foot-list li::before{content:"»";position:absolute;left:0;color:var(--pink);font-size:14px;top:-1px}
.divider{position:absolute;width:3px;height:32px;background:var(--pink)}
.social{position:absolute;width:27px;height:27px;border-radius:50%;background:var(--white)}
</style>
</head>
<body>

<!-- Hero -->
<section class="hero">
  <div class="hero-photo" role="img" aria-label="Photo of a group sitting cross-legged on yoga mats on a lawn at sunset"></div>
  <div class="hero-shade"></div>
  <div class="brand" style="left:172px;top:15px">Velka Haven</div>
  <nav class="nav">
    <a style="left:540px">Home</a>
    <a style="left:621px">About</a>
    <a style="left:706px">Services</a>
    <a style="left:807px">Contact</a>
  </nav>
  <div class="btn" style="left:899px;top:15px;width:131px;height:42px;font-size:16px">Book Now</div>
  <svg class="arrow" style="left:172px" width="24" height="40" viewBox="0 0 24 40"><path d="M20 2 L4 20 L20 38" fill="none" stroke="#fff" stroke-width="2"/></svg>
  <svg class="arrow" style="left:1004px" width="24" height="40" viewBox="0 0 24 40"><path d="M4 2 L20 20 L4 38" fill="none" stroke="#fff" stroke-width="2"/></svg>
  <h1 class="hero-title">YOGA AND<br>PILATES</h1>
  <p class="hero-sub">I teach privates and small groups</p>
  <div class="btn" style="left:532px;top:443px;width:131px;height:40px;font-size:16px">Know More</div>
  <svg class="abs" style="left:0;top:620px" width="1200" height="80" viewBox="0 0 1200 80">
    <path d="M0 68 Q600 -20 1200 68 L1200 80 L0 80 Z" fill="#e8877f"/>
    <path d="M0 82 Q600 -2 1200 82 L1200 80 L0 80 Z" fill="#ffffff"/>
  </svg>
</section>

<!-- About -->
<h2 class="about-heading">About<br><span>VELKA<br>HAVEN</span></h2>
<p class="about-note">Sed do eiusmod temor incididunt ut labore et</p>
<div class="photo" style="left:460px;top:730px;width:280px;height:378px;background:linear-gradient(160deg,#f2f1ee 0%,#dcdad5 55%,#8a8782 100%);box-shadow:0 8px 24px rgba(0,0,0,.15)" role="img" aria-label="Photo of a woman in a side-angle yoga stretch in a bright studio"></div>
<div class="photo" style="left:606px;top:982px;width:315px;height:214px;border:3px solid var(--pink);background:linear-gradient(180deg,#e9e4dd 0%,#cfc6bc 55%,#6b5d66 100%)" role="img" aria-label="Photo of three women meditating on mats in a studio"></div>
<p class="about-text">Lorem ipsum dolt amet, consectetur adipiscing elit, sed do eiusmod tempor incididunt ut labore et dolore magna aliqua. Quis ipsum suspendisse ultrices gravida. Risus commodo viverra manas</p>
<div class="btn" style="left:767px;top:905px;width:131px;height:42px;font-size:16px">Read More</div>

<!-- Weekly Classes -->
<section class="classes">
  <h2 class="section-title" style="top:32px;color:var(--white)">Weekly Classes</h2>
  <p class="section-lead" style="top:94px;color:var(--white)">Lorem ipsum dolor sit amet, consectetur adipiscing elit. Cras facilisis metus<br>id ex mollis, a mollis sapien tristique. Ut eu nibh in urna vulputate efficitur.</p>

  <div class="card" style="left:172px;top:175px"><div class="card-photo" role="img" aria-label="Photo of a class lying on mats with legs raised" style="background:linear-gradient(180deg,#e8e8e8,#bdbdbd 70%,#6a6a6a)"></div><h3>Nunc vestibulum</h3><p>Lorem ipsum dolt a consectetur adipiscing</p><span class="more">Read More ▸</span></div>
  <div class="card" style="left:466px;top:175px"><div class="card-photo" role="img" aria-label="Photo of a group in triangle pose in a studio" style="background:linear-gradient(180deg,#5e5a55,#8a8176 60%,#3a3836)"></div><h3>Nunc vestibulum</h3><p>Lorem ipsum dolt a consectetur adipiscing</p><span class="more">Read More ▸</span></div>
  <div class="card" style="left:760px;top:175px"><div class="card-photo" role="img" aria-label="Photo of a class holding side planks" style="background:linear-gradient(180deg,#7b7b80,#a5a5aa 55%,#4a4a50)"></div><h3>Nunc vestibulum</h3><p>Lorem ipsum dolt a consectetur adipiscing</p><span class="more">Read More ▸</span></div>

  <div class="card" style="left:172px;top:520px"><div class="card-photo" role="img" aria-label="Photo of women meditating side by side" style="background:linear-gradient(180deg,#efe9e6,#d9b7b3 55%,#6d5c60)"></div><h3>Nunc vestibulum</h3><p>Lorem ipsum dolt a consectetur adipiscing</p><span class="more">Read More ▸</span></div>
  <div class="card" style="left:466px;top:520px"><div class="card-photo" role="img" aria-label="Photo of a woman in a forearm balance" style="background:linear-gradient(180deg,#f5f5f5,#e6e6e6 65%,#555)"></div><h3>Nunc vestibulum</h3><p>Lorem ipsum dolt a consectetur adipiscing</p><span class="more">Read More ▸</span></div>
  <div class="card" style="left:760px;top:520px"><div class="card-photo" role="img" aria-label="Photo of a group stretching in a warm studio" style="background:linear-gradient(180deg,#d8c7b2,#b9a58e 55%,#514a48)"></div><h3>Nunc vestibulum</h3><p>Lorem ipsum dolt a consectetur adipiscing</p><span class="more">Read More ▸</span></div>

  <div class="btn" style="left:499px;top:854px;width:199px;height:40px;font-size:15px;background:var(--white);color:var(--pink);box-shadow:3px 3px 0 rgba(255,255,255,.5);font-weight:500">View More Our Classes</div>
</section>

<!-- Benefits -->
<section class="benefits">
  <h2 class="section-title" style="top:50px">Benefits Of Yoga and Pilates</h2>
  <p class="section-lead" style="top:130px;color:#222">Lorem ipsum dolor sit amet, consectetur adipiscing elit. Cras facilisis metus id ex mollis, a mollis<br>sapien tristique. Ut eu nibh in urna vulputate efficitur.</p>
  <svg class="abs" style="left:389px;top:297px" width="422" height="422" viewBox="0 0 422 422"><circle cx="211" cy="211" r="209" fill="none" stroke="#777" stroke-width="1.2" stroke-dasharray="3 3"/></svg>
  <div class="abs" style="left:424px;top:192px;width:332px;height:527px;border-radius:160px 160px 110px 110px;background:radial-gradient(ellipse at 50% 40%,#d8c1b2 0%,#b9a39a 35%,#6d6d72 70%,rgba(40,40,45,.9) 100%)" role="img" aria-label="Photo of a woman in lotus pose with hands joined overhead"></div>

  <div class="benefit" style="left:145px;top:340px;text-align:right;width:220px"><h4>Be Happy</h4><p>Lorem ipsum dolt amet,<br>consectetur adipiscing</p></div>
  <div class="icon-dot" style="left:392px;top:337px"><svg width="40" height="40" viewBox="0 0 40 40"><circle cx="20" cy="20" r="7" fill="none" stroke="#fff" stroke-width="2"/><path d="M20 4v6M20 30v6M4 20h6M30 20h6M9 9l4 4M27 27l4 4M9 31l4-4M27 13l4-4" stroke="#fff" stroke-width="2"/></svg></div>

  <div class="benefit" style="left:829px;top:340px"><h4>Erase Pain</h4><p>Lorem ipsum dolt amet,<br>consectetur adipiscing</p></div>
  <div class="icon-dot" style="left:732px;top:337px"><svg width="40" height="40" viewBox="0 0 40 40"><path d="M20 6v28M12 12h16M11 20h18M12 28h16" stroke="#fff" stroke-width="2" fill="none"/></svg></div>

  <div class="benefit" style="left:120px;top:470px;text-align:right"><h4>Stay Balanced</h4><p>Lorem ipsum dolt amet,<br>consectetur adipiscing</p></div>
  <div class="icon-dot" style="left:349px;top:468px"><svg width="44" height="36" viewBox="0 0 44 36"><path d="M22 4 C28 12 28 22 22 30 C16 22 16 12 22 4Z M22 30 C14 30 8 24 6 16 C14 16 20 22 22 30Z M22 30 C30 30 36 24 38 16 C30 16 24 22 22 30Z" fill="none" stroke="#fff" stroke-width="2"/></svg></div>

  <div class="benefit" style="left:866px;top:470px"><h4>Treat Arthritis</h4><p>Lorem ipsum dolt amet,<br>consectetur adipiscing</p></div>
  <div class="icon-dot" style="left:772px;top:468px"><svg width="40" height="40" viewBox="0 0 40 40"><path d="M8 32h24M14 32l6-12 8-10M20 20l8 4" stroke="#fff" stroke-width="2.4" fill="none" stroke-linecap="round"/><circle cx="29" cy="8" r="3" fill="#fff"/></svg></div>
</section>

<!-- Get In Touch -->
<section class="contact">
  <h2 class="section-title" style="top:44px;color:var(--white)">Get In Touch</h2>

  <div class="info-dot" style="left:217px;top:141px"><svg width="20" height="26" viewBox="0 0 20 26"><path d="M10 1C5 1 1 5 1 10c0 6 9 15 9 15s9-9 9-15c0-5-4-9-9-9z" fill="#e8877f"/><circle cx="10" cy="10" r="3.2" fill="#fff"/></svg></div>
  <div class="info" style="left:291px;top:131px"><b>ADDRESS</b>48 Lark Lane, 9 Meadow Row,<br>Fairbrook, FB 40211-3300</div>

  <div class="info-dot" style="left:530px;top:141px"><svg width="22" height="22" viewBox="0 0 24 24"><path d="M6.6 10.8a15 15 0 0 0 6.6 6.6l2.2-2.2a1 1 0 0 1 1-.25 11.4 11.4 0 0 0 3.6.57 1 1 0 0 1 1 1V20a1 1 0 0 1-1 1A17 17 0 0 1 3 4a1 1 0 0 1 1-1h3.5a1 1 0 0 1 1 1c0 1.25.2 2.45.57 3.57a1 1 0 0 1-.25 1z" fill="#e8877f"/></svg></div>
  <div class="info" style="left:604px;top:131px"><b>PHONE</b>01 555 204 118<br>00 555 307 226</div>

  <div class="info-dot" style="left:772px;top:141px"><svg width="22" height="18" viewBox="0 0 22 18"><rect x="1" y="2" width="20" height="14" rx="2" fill="#e8877f"/><path d="M2 3l9 7 9-7" stroke="#fff" stroke-width="1.8" fill="none"/></svg></div>
  <div class="info" style="left:845px;top:131px"><b>E-MAIL</b>hello@velkahaven.com</div>

  <div class="form-panel">
    <h3 style="position:absolute;left:0;width:800px;top:22px;text-align:center;color:var(--white);font-weight:400;font-size:34px">Contact Us</h3>
    <div class="field" style="left:43px;top:77px;width:234px;height:39px">Your Name</div>
    <div class="field" style="left:284px;top:77px;width:234px;height:39px">Email Address</div>
    <div class="field" style="left:528px;top:77px;width:233px;height:39px">Phone</div>
    <div class="field" style="left:43px;top:126px;width:718px;height:121px">Message</div>
    <div class="btn" style="left:314px;top:262px;width:169px;height:41px;font-size:16px;background:var(--white);color:var(--pink);box-shadow:3px 3px 0 rgba(255,255,255,.5);font-weight:500">Send A Message</div>
  </div>
</section>

<!-- Footer -->
<footer class="footer">
  <svg class="abs" style="left:0;top:0" width="1200" height="344" viewBox="0 0 1200 344">
    <rect x="0" y="0" width="1200" height="70" fill="#e8877f"/>
    <path d="M0 70 Q600 -8 1200 70 Z" fill="#f6958d"/>
    <path d="M0 72 Q600 10 1200 72 L1200 344 L0 344 Z" fill="#e8877f"/>
    <path d="M0 86 Q600 22 1200 86 L1200 344 L0 344 Z" fill="#1b1b1b"/>
  </svg>
  <div class="brand" style="left:172px;top:100px;color:var(--white)">Velka Haven</div>
  <p class="abs" style="left:172px;top:142px;width:240px;font-size:13.5px;line-height:21px;color:#d6d6d6">Curabitur pulvinar, hen imperdiet, felis nulla blandit leo, ac tincidunt orci nunc a orci. Quisque ex tellus, dictum vulpate nisl at, lucs lobortis tortor.</p>
  <p class="abs" style="left:172px;top:254px;font-size:12.5px;color:#8c8c8c">© 2022 <span style="color:var(--pink)">Velka Haven</span>. All right reserved</p>

  <div class="divider" style="left:434px;top:125px"></div>
  <div class="foot-col abs" style="left:483px;top:100px"><h5>Quick Links</h5>
    <ul class="foot-list"><li>Home</li><li>About</li><li>Services</li><li>Contact</li></ul></div>

  <div class="divider" style="left:600px;top:125px"></div>
  <div class="foot-col abs" style="left:635px;top:100px"><h5>Our Classes</h5>
    <ul class="foot-list"><li>Mauris maximus</li><li>Quam at viverra</li><li>Tempor Integer a</li><li>Donec iaculis ante</li></ul></div>

  <div class="divider" style="left:796px;top:125px"></div>
  <div class="foot-col abs" style="left:834px;top:100px"><h5>Newsletter</h5></div>
  <div class="abs" style="left:834px;top:132px;width:194px;height:34px;background:var(--white);font-size:11px;color:#666;display:flex;align-items:center;padding-left:9px;gap:6px">
    <svg width="12" height="9" viewBox="0 0 12 9"><rect x=".5" y=".5" width="11" height="8" fill="none" stroke="#888"/><path d="M1 1l5 4 5-4" stroke="#888" fill="none"/></svg>Enter Email Address</div>
  <div class="abs" style="left:834px;top:176px;width:194px;height:34px;background:var(--pink-button);color:var(--white);font-size:13px;font-weight:500;display:flex;align-items:center;justify-content:center">Subscribe</div>
  <div class="social" style="left:834px;top:236px"></div>
  <div class="social" style="left:871px;top:236px"></div>
  <div class="social" style="left:908px;top:236px"></div>
  <div class="social" style="left:945px;top:236px"></div>
</footer>

</body>
</html>
```